Herausgeber suchen Design
Zielgruppe
Wir sind Herausgeber einer Festschrift für unseren Doktor-/Habilvater, Prof. Dr. Lohmeyer, und suchen ein hochwertiges Design für die Einladungskarten zu einem Symposium, im Rahmen dessen die Festschrift übergeben wird; Zielgruppe sind die Autoren der Festschrift, Alumnis und Weggefährten von Herrn Lohmeyer
Aufgabenstellung
- Maße: 210 mm x 105 mm
- Einladungskarte: geklappt; Frontseite, 2 Innenseiten, Rückseite
- Zum Text siehe Datei 'Text Einladungskarte'
- Design eher traditionell/konservativ, da es sich um einen wissenschaftlichen Hintergrund handelt (Symposium, Übergabe Festschrift)
- Die Farben sollen mit dem Cover der Festschrift korrespondieren (vgl. Datei 'Templates_Research_Vossek', dort das erste Cover (KLM_RE_T01)

```html
<!DOCTYPE html>
<html lang="de">
<head>
<meta charset="utf-8">
<title>Einladung – Symposium und Übergabe der Festschrift</title>
<link rel="stylesheet" href="https://fonts.googleapis.com/css2?family=Source+Sans+3:wght@300;400&display=swap">
<style>
  :root {
    --backdrop: #dfe3e6;
    --back-blue-top: #0b4a8f;
    --back-blue-bottom: #0d5aa3;
    --band-blue: #1f72b6;
    --band-navy: #2b3758;
    --rule-white: #e9eef5;
    --text-white: #f4f6fa;
    --panel-w: 360px;
    --panel-h: 720px;
  }
  * { box-sizing: border-box; margin: 0; padding: 0; }
  html, body {
    width: 1200px;
    height: 840px;
    overflow: hidden;
  }
  body {
    background: var(--backdrop);
    display: flex;
    align-items: center;
    justify-content: center;
    font-family: "Source Sans 3", "Helvetica Neue", Arial, sans-serif;
  }
  .card-spread {
    display: flex;
    width: calc(var(--panel-w) * 2);
    height: var(--panel-h);
    box-shadow: 0 10px 30px rgba(20, 35, 60, 0.25);
  }
  .panel {
    position: relative;
    width: var(--panel-w);
    height: var(--panel-h);
    overflow: hidden;
  }
  .panel-back {
    background: linear-gradient(180deg, var(--back-blue-top), var(--back-blue-bottom));
  }
  .panel-front {
    display: flex;
  }
  .band-light {
    width: 44%;
    height: 100%;
    background: var(--band-blue);
  }
  .band-dark {
    position: relative;
    flex: 1;
    height: 100%;
    background: var(--band-navy);
  }
  .rule {
    position: absolute;
    bottom: 62px;
    height: 1.5px;
    background: var(--rule-white);
  }
  .panel-back .rule { left: 0; right: 0; }
  .panel-front .rule { left: 0; width: 74%; }
  .title {
    position: absolute;
    left: 50%;
    top: 100px;
    transform-origin: left top;
    transform: translate(-18px, 210px) rotate(-90deg);
    color: var(--text-white);
    font-weight: 400;
    font-size: 46px;
    letter-spacing: 0.5px;
    white-space: nowrap;
  }
</style>
</head>
<body>
  <main class="card-spread">
    <section class="panel panel-back" aria-label="Rückseite">
      <div class="rule"></div>
    </section>
    <section class="panel panel-front" aria-label="Frontseite">
      <div class="band-light"></div>
      <div class="band-dark">
        <h1 class="title">Einladung</h1>
      </div>
      <div class="rule"></div>
    </section>
  </main>
</body>
</html>
```